Velvet corsaro

I want a business card design. the company is an infrastructure development company.

Target Market(s)

Government
real estate investors
real estate clients

Industry/Entity Type

Business

```html
<!DOCTYPE html>
<html lang="en">
<head>
<meta charset="utf-8">
<title>Velvet Corsaro – Business Card</title>
<link rel="stylesheet" href="https://fonts.googleapis.com/css2?family=Arimo:wght@400;700&family=Exo+2:wght@600&display=swap">
<style>
  :root {
    --brand-red: #e8323a;
    --brand-blue: #0fb0ec;
    --card-white: #ffffff;
    --page-bg: #ffffff;
    --text-white: #ffffff;
    --card-shadow: rgba(0, 0, 0, 0.55);
  }
  html, body {
    margin: 0;
    padding: 0;
    overflow: hidden;
    background: var(--page-bg);
  }
  .canvas {
    position: relative;
    width: 1200px;
    height: 887px;
    overflow: hidden;
    background: var(--page-bg);
  }
  .card {
    position: absolute;
    background: var(--card-white);
    box-shadow: 6px 7px 9px var(--card-shadow);
    overflow: hidden;
  }
  .card--front { left: 68px; top: 30px; width: 660px; height: 396px; }
  .card--back  { left: 62px; top: 450px; width: 666px; height: 402px; }

  .wordmark {
    position: absolute;
    display: flex;
    align-items: center;
    gap: 14px;
    font-family: "Arimo", Arial, sans-serif;
    font-weight: 700;
    color: var(--brand-red);
    letter-spacing: 1px;
    white-space: nowrap;
  }
  .wordmark__square {
    width: 30px;
    height: 30px;
    background: var(--brand-blue);
  }
  .card--front .wordmark { left: 148px; top: 176px; font-size: 40px; }
  .card--back .wordmark  { left: 170px; top: 90px;  font-size: 34px; }
  .card--back .wordmark__square { width: 26px; height: 26px; }

  .card__band {
    position: absolute;
    left: 0;
    top: 198px;
    width: 100%;
    height: 204px;
    background: var(--brand-blue);
  }
  .contact {
    position: absolute;
    left: 330px;
    top: 205px;
    width: 370px;
    text-align: center;
    font-family: "Arimo", Arial, sans-serif;
    color: var(--text-white);
    line-height: 1.12;
  }
  .contact__heading {
    margin: 0;
    font-size: 14px;
    font-weight: 400;
    color: var(--brand-red);
    text-transform: uppercase;
  }
  .contact__heading--company { margin-top: 7px; }
  .contact p { margin: 0; font-size: 13.5px; }
  .contact .contact__phone { font-size: 11px; }

  .spec-notes {
    position: absolute;
    left: 836px;
    top: 92px;
    width: 350px;
    font-family: "Exo 2", Arial, sans-serif;
    font-weight: 600;
    font-size: 40px;
    line-height: 59px;
    color: var(--brand-red);
  }
  .spec-notes p { margin: 0; }
  .spec-notes .spec-notes__gap { margin-top: 22px; }
</style>
</head>
<body>
<main class="canvas">
  <section class="card card--front" aria-label="Card front">
    <div class="wordmark"><span class="wordmark__square"></span>VELVET CORSARO</div>
  </section>

  <section class="card card--back" aria-label="Card back">
    <div class="wordmark"><span class="wordmark__square"></span>VELVET CORSARO</div>
    <div class="card__band"></div>
    <div class="contact">
      <h3 class="contact__heading">My Details</h3>
      <p>Kayode Balogun</p>
      <p>MD.</p>
      <p class="contact__phone">+234 8010245678, +234 7031169842</p>
      <p>kayode@velvetcorsaro.com</p>
      <h3 class="contact__heading contact__heading--company">Company Details</h3>
      <p>12, Harbour Lane, Off Marina Crescent Road,</p>
      <p>Yaba Lagos, Nigeria</p>
      <p>+23412250417, +2347059183026</p>
      <p>info@velvetcorsaro.com</p>
      <p>www.velvetcorsaro.com</p>
    </div>
  </section>

  <aside class="spec-notes">
    <p>90mm x 55x</p>
    <p>Business Card</p>
    <p>Size</p>
    <p class="spec-notes__gap">*Double-sided</p>
    <p class="spec-notes__gap">Right side info</p>
    <p>Business Card</p>
    <p>Design</p>
    <p class="spec-notes__gap">*Landscape</p>
  </aside>
</main>
</body>
</html>
```